Meridel Advisory & Coaching Collective Web Site Design

Help!

We have started designing and building a Web site to promote and sell training services to HR managers. But we are not very good designers. In fact, we stink.

We have a logo.

We have most of the content (more or less) and the site architecture. But we have put together a pretty lousy look and feel.

Take a look: http://brightlowpath.example/vortalindex.html

What we'd like is a Web 3.0 type design - clean, simple, modern looking. Some sites we admire:

pinvale.example
trelosk.example
skivorn.example
quibbledot.example
morpa.example

We have access to stock photography, some of which we've used on the site we've built so far. You can use those and others. But keep it simple.

Target Market(s)

Professional HR managers in larger companies

Requirements
Must have
• Use our logo and a color scheme based off of it. Logo file uploaded.

Need to see home page and examples of secondary pages, based on site currently online.

```html
<!DOCTYPE html>
<html lang="en">
<head>
<meta charset="utf-8">
<title>Meridel Advisory & Coaching Collective</title>
<link href="https://fonts.googleapis.com/css2?family=Arimo:wght@400;700&display=swap" rel="stylesheet">
<style>
  :root {
    --accent: #f26a4f;
    --ink: #1e1e1e;
    --text: #555555;
    --muted: #8a8a8a;
    --page: #e6e6e6;
    --page-light: #f8f8f8;
    --line: #d2d2d2;
    --footer: #232323;
    --footer-text: #d8d8d8;
    --footer-link: #7a7a7a;
    --white: #ffffff;
  }
  * { box-sizing: border-box; margin: 0; padding: 0; }
  html, body { width: 900px; height: 1200px; overflow: hidden; background: var(--white); }
  body { font-family: "Arimo", Arial, sans-serif; color: var(--text); position: relative; }

  .page {
    position: absolute; left: 34px; top: 0; width: 830px; height: 1200px;
    background: radial-gradient(ellipse 520px 420px at 330px 260px, var(--page-light), var(--page) 75%);
  }
  .abs { position: absolute; }

  /* Brand */
  .brand { left: 74px; top: 76px; display: flex; align-items: center; gap: 10px; }
  .brand-dot { width: 22px; height: 22px; border-radius: 50%; background: var(--accent); }
  .brand-name { font-size: 29px; color: var(--ink); font-weight: 400; letter-spacing: -0.5px; }

  /* Hero */
  .hero-title { left: 138px; top: 183px; font-weight: 700; line-height: 34px; font-size: 37px; letter-spacing: -1px; }
  .hero-title .dark { color: var(--ink); display: block; }
  .hero-title .bright { color: var(--accent); display: block; }
  .hero-sub { left: 139px; top: 255px; font-size: 16px; color: var(--ink); line-height: 18px; }
  .slider-dots { left: 137px; top: 314px; display: flex; gap: 5px; }
  .slider-dots span { width: 11px; height: 11px; border-radius: 50%; background: #d4d4d4; }
  .slider-dots span.on { width: 12px; height: 12px; background: var(--accent); }
  .hero-photo {
    left: 476px; top: 10px; width: 276px; height: 403px;
    background: linear-gradient(180deg, #cfcfcf 0%, #9a9a9a 40%, #2c2c2c 75%, #3a3a3a 100%);
    border-radius: 120px 120px 10px 10px;
  }
  .start-btn {
    left: 389px; top: 170px; width: 144px; height: 144px; border-radius: 50%;
    background: var(--accent); color: var(--white); font-weight: 700; font-size: 19px;
    display: flex; align-items: center; justify-content: center; text-align: center; line-height: 19px;
  }

  /* Nav */
  .nav { left: 137px; top: 413px; width: 620px; height: 58px; display: flex;
    background: linear-gradient(#f1f1f1, #dcdcdc); border: 1px solid #cfcfcf; }
  .nav a { flex: 1; display: flex; align-items: center; justify-content: center;
    font-size: 10px; color: #333; text-decoration: none; border-right: 1px solid #c9c9c9; }
  .nav a:last-child { border-right: none; }
  .nav a.current { background: var(--accent); color: var(--white); }

  /* Feature cards */
  .feature { width: 199px; top: 507px; }
  .feature h3 { font-size: 15px; font-weight: 400; color: var(--ink); text-align: center; height: 23px; }
  .feature .thumb { height: 84px; border: 1px solid #cfcfcf; border-radius: 3px;
    background: linear-gradient(135deg, #f2f2f2, #a8a8a8); }
  .feature .more { font-size: 7px; color: #444; margin-top: 14px; letter-spacing: 0.3px; }

  /* Banner */
  .rule { height: 1px; background: var(--line); }
  .banner-text { left: 140px; top: 689px; font-size: 14.5px; line-height: 19px; color: #6d6d6d; }
  .join-btn { left: 614px; top: 683px; width: 146px; height: 47px; border: 1px solid #c6c6c6; border-radius: 3px;
    background: linear-gradient(#e6e6e6, #cfcfcf); display: flex; align-items: center; justify-content: center;
    font-size: 14px; color: #222; }

  /* Content */
  .block-title { font-size: 14.5px; color: #2a2a2a; letter-spacing: 0.2px; }
  .block-body { font-size: 8px; line-height: 12px; color: var(--muted); width: 360px; }
  .block-more { font-size: 8.5px; color: #333; }
  .news-item { left: 563px; width: 200px; display: flex; gap: 10px; }
  .news-thumb { width: 56px; height: 56px; border-radius: 4px; border: 1px solid #ccc;
    background: linear-gradient(135deg, #f0f0f0, #8e8e8e); flex: none; }
  .news-date { font-size: 7px; color: #666; margin-top: 4px; }
  .news-head { font-size: 8px; color: var(--accent); margin-top: 4px; }
  .news-text { font-size: 8px; color: var(--muted); line-height: 12px; }

  /* Footer */
  .footer { left: 0; top: 1063px; width: 830px; height: 137px; background: var(--footer); }
  .foot-col { top: 42px; }
  .foot-col h4 { font-size: 9px; font-weight: 400; color: var(--footer-text); letter-spacing: 0.6px; margin-bottom: 14px; }
  .foot-col li { list-style: none; font-size: 6px; color: var(--footer-link); letter-spacing: 0.6px; line-height: 13.4px; }
  .foot-col li::before { content: "• "; }
  .news-note { font-size: 6px; color: #5e5e5e; letter-spacing: 0.5px; }
  .email-field { width: 148px; height: 20px; border: 1px solid #555; background: #1a1a1a; }
  .email-go { width: 20px; height: 20px; background: var(--accent); display: flex; align-items: center; justify-content: center; }
  .unsub { font-size: 6px; color: var(--accent); text-decoration: underline; letter-spacing: 0.5px; }
</style>
</head>
<body>
<div class="page">
  <div class="abs brand" style="left:40px">
    <span class="brand-dot"></span>
    <span class="brand-name">Meridel Advisory …for Halvern HR Guild</span>
  </div>

  <div class="abs hero-photo" style="left:442px" role="img" aria-label="Smiling businessman in dark suit with arms crossed"></div>

  <h1 class="abs hero-title" style="left:104px"><span class="dark">FRESH</span><span class="bright">SOLUTIONS</span></h1>
  <p class="abs hero-sub" style="left:105px">Generational Tools &amp; Training<br>for HR Professionals</p>
  <div class="abs slider-dots" style="left:103px"><span class="on"></span><span></span><span></span></div>
  <div class="abs start-btn" style="left:355px">START<br>NOW!</div>

  <nav class="abs nav" style="left:103px">
    <a class="current" href="#">HOME</a><a href="#">ABOUT</a><a href="#">RESOURCES</a><a href="#">TOOLS</a><a href="#">TRAINING</a><a href="#">DISCUSS</a>
  </nav>

  <section class="abs feature" style="left:105px">
    <h3>Generations 101</h3>
    <div class="thumb" role="img" aria-label="Group of smiling colleagues"></div>
    <p class="more">READ MORE</p>
  </section>
  <section class="abs feature" style="left:316px">
    <h3>Generation Gaps</h3>
    <div class="thumb" role="img" aria-label="Smiling man close-up"></div>
    <p class="more">READ MORE</p>
  </section>
  <section class="abs feature" style="left:528px">
    <h3>Gen Strategies</h3>
    <div class="thumb" role="img" aria-label="Interlocking metal gears"></div>
    <p class="more">READ MORE</p>
  </section>

  <div class="abs rule" style="left:105px; top:661px; width:621px"></div>
  <p class="abs banner-text" style="left:106px">ENSURING THE HIGHEST LEVEL OF CUSTOMERS SATISFACTION<br>WHAT MAKES US A BETTER COMPANY IN OUR FIELD</p>
  <div class="abs join-btn" style="left:580px">JOIN US NOW!</div>
  <div class="abs rule" style="left:105px; top:750px; width:621px"></div>
  <div class="abs rule" style="left:0; top:784px; width:830px; background:#bdbdbd"></div>

  <svg class="abs" style="left:106px; top:787px" width="19" height="19" viewBox="0 0 19 19">
    <rect x="1.5" y="3.5" width="13" height="13" fill="none" stroke="#f26a4f" stroke-width="2"/>
    <path d="M7 11 L16 2 L18 4 L9 13 L6.5 13.5 Z" fill="#f26a4f"/>
  </svg>
  <h2 class="abs block-title" style="left:141px; top:785px">OUR CUSTOMERS ARE OUR PRIORITY</h2>
  <p class="abs block-body" style="left:141px; top:814px">At nequ eget nisus leo vel nean necoum epsum prin faucibus oposuere cubind ise olltu dinvelit sed le pharetr.unt arra selorta diam eiiscing aliqln pde aliquet sit amet euismod iuor ut ligulam dapibus tincidunt melit. Fusc ismod conse quat aris accun ipm dolor sie adicing elite sed dolor.Aliqua rgue fermentum nisl. Mauris acml diaed in lacu.</p>
  <p class="abs block-more" style="left:141px; top:874px">Read more</p>

  <svg class="abs" style="left:106px; top:912px" width="19" height="15" viewBox="0 0 19 15">
    <path d="M0 2 H6 L8 4 H17 V6 H4 L1 15 H0 Z" fill="#f26a4f"/>
    <path d="M4.5 7 H19 L16 15 H1.5 Z" fill="#f26a4f"/>
  </svg>
  <h2 class="abs block-title" style="left:141px; top:911px">WE DON’T PROMISE – WE ACT</h2>
  <p class="abs block-body" style="left:141px; top:940px">At nequ eget nisus leo vel nean necoum epsum prin faucibus oposuere cubind ise olltu dinvelit sed le pharetr.unt arra selorta diam eiiscing aliqln pde aliquet sit amet euismod iuor ut ligulam dapibus tincidunt melit. Fusc ismod conse quat aris accun ipm dolor sie adicing elite sed dolor.Aliqua rgue fermentum nisl. Mauris acml diaed in lacu.</p>
  <p class="abs block-more" style="left:141px; top:1000px">Read more</p>

  <h2 class="abs block-title" style="left:529px; top:785px">WHAT`S NEW?</h2>
  <article class="abs news-item" style="left:529px; top:819px">
    <div class="news-thumb" role="img" aria-label="Portrait of a young man"></div>
    <div><p class="news-date">21 JUNE</p><p class="news-head">Lorem ipsum dolor sit amet</p><p class="news-text">Faucibus oposuere cun olltvelit sed le pharuars elorta diam.</p></div>
  </article>
  <article class="abs news-item" style="left:529px; top:888px">
    <div class="news-thumb" role="img" aria-label="Portrait of a smiling man"></div>
    <div><p class="news-date">19 MAY</p><p class="news-head">At nequ eget nisuleo vel</p><p class="news-text">Faucibus oposuere cun olltvelit sed le pharuars elorta diam.</p></div>
  </article>
  <article class="abs news-item" style="left:529px; top:957px">
    <div class="news-thumb" role="img" aria-label="Portrait of an older man"></div>
    <div><p class="news-date">17 APRIL</p><p class="news-head">Integer rutrum ante eu</p><p class="news-text">Faucibus oposuere cun olltvelit sed le pharuars elorta diam.</p></div>
  </article>

  <footer class="abs footer">
    <div class="abs foot-col" style="left:106px"><h4>COMPANY</h4><ul><li>ABOUT US</li><li>SERVICES</li><li>PRESENTATION</li><li>CLIENTS</li></ul></div>
    <div class="abs foot-col" style="left:205px"><h4>SERVICES</h4><ul><li>DEVELOPMENT</li><li>RESEARCH</li><li>PLANNING</li></ul></div>
    <div class="abs foot-col" style="left:304px"><h4>ADVICE</h4><ul><li>FAQS</li><li>SUPPORT</li></ul></div>
    <div class="abs foot-col" style="left:403px"><h4>FOR CLIENTS</h4><ul><li>SIGN IN</li><li>FORUMS</li><li>PROMOTIONS</li></ul></div>
    <div class="abs foot-col" style="left:515px">
      <h4>NEWSLETTER</h4>
      <p class="news-note">ENTER YOUR EMAIL TO JOIN OUR MAILING LIST</p>
      <div style="display:flex; gap:3px; margin-top:8px">
        <div class="email-field"></div>
        <div class="email-go"><svg width="6" height="6" viewBox="0 0 6 6"><path d="M1 0 L5 3 L1 6 Z" fill="#fff"/></svg></div>
      </div>
      <p class="unsub" style="margin-top:7px">UNSUBSCRIBE</p>
    </div>
  </footer>
</div>
</body>
</html>
```